sticker of engine oil bottle

Dear Designers
i want to design new sticker for my bottle engine oil brand
i want the sticker creative and get harmonic with the bottle color one Blue and another color Red
my brand name is (Vesko) as attached logo and pictures and i will attached pictures you can take ideas from it
The Shape of Plastic bottle i used is the first bottle attached in blue color Vesko 20W50 and in red color vesko 5W30
i want new creative design calms colors and designs
and not copy paste from another design

Target Market(s)

car care and engine oil service centers

Requirements
Must have
• companies approvals and certificates
Nice to have
• new idea
Should not have
• copy past from another design on internet

```html
<!DOCTYPE html>
<html lang="en">
<head>
<meta charset="utf-8">
<title>Vesko Lubricants – Oil Bottle Stickers</title>
<link rel="stylesheet" href="https://fonts.googleapis.com/css2?family=Poppins:wght@400;500;600;700;800&display=swap">
<style>
  :root {
    --page: #ffffff;
    --ink: #1c1c24;
    --white: #ffffff;
    --red-deep: #560008;
    --red: #b3202f;
    --red-bright: #c8283a;
    --blue-deep: #1b2756;
    --blue: #2b5b9f;
    --blue-bright: #2f67b3;
    --silver-light: #f4f4f4;
    --silver-mid: #bdbdbd;
    --silver-dark: #8a8a8a;
    --label-top: #ffffff;
    --label-bottom: #c9c9cb;
    --badge-gold: #d3ad55;
    --badge-grey: #9a9a9a;
    --badge-green: #4c7a5a;
  }
  html, body {
    margin: 0;
    padding: 0;
    width: 953px;
    height: 1200px;
    overflow: hidden;
    background: var(--page);
  }
  .sheet {
    position: relative;
    width: 953px;
    height: 1200px;
    font-family: "Poppins", sans-serif;
  }
  .sticker {
    position: absolute;
    top: 330px;
    width: 442px;
    height: 533px;
    filter: drop-shadow(0 4px 6px rgba(0,0,0,0.25));
  }
  .sticker--red { left: 20px; }
  .sticker--blue { left: 491px; }
  .sticker svg { width: 100%; height: 100%; display: block; overflow: visible; }
  .brand-name { font-weight: 800; font-size: 66px; fill: var(--white); letter-spacing: 1px; }
  .range-title { font-weight: 700; font-size: 46px; fill: var(--white); letter-spacing: 1px; }
  .feature { font-weight: 400; font-size: 16.5px; fill: var(--white); }
  .seal-name { font-weight: 800; font-size: 40px; }
  .volume { font-weight: 700; font-size: 33px; fill: var(--white); }
  .spec { font-weight: 600; font-size: 18px; fill: var(--ink); }
  .spec-base { font-weight: 600; font-size: 18px; fill: var(--red); }
  .grade { font-weight: 800; font-size: 124px; letter-spacing: -2px; }
  .meets { font-weight: 600; font-size: 15.5px; fill: var(--red-bright); }
  .approvals { font-weight: 600; font-size: 12.6px; fill: var(--ink); }
</style>
</head>
<body>
<main class="sheet">

  <!-- Red sticker: 5W30 -->
  <section class="sticker sticker--red" aria-label="Vesko 5W30 sticker">
    <svg viewBox="0 0 680 820" xmlns="http://www.w3.org/2000/svg">
      <defs>
        <clipPath id="red-shape">
          <path d="M0,45 Q0,0 45,2 L360,40 Q405,50 418,92 L658,710 Q678,772 610,777 L75,800 Q35,802 32,760 L5,120 Z"/>
        </clipPath>
        <linearGradient id="red-paper" x1="0" y1="0" x2="0" y2="1">
          <stop offset="0.35" stop-color="var(--label-top)"/>
          <stop offset="1" stop-color="var(--label-bottom)"/>
        </linearGradient>
        <linearGradient id="red-band" x1="0" y1="0" x2="0" y2="1">
          <stop offset="0" stop-color="var(--red-deep)"/>
          <stop offset="1" stop-color="var(--red)"/>
        </linearGradient>
        <linearGradient id="red-silver" x1="0" y1="0" x2="1" y2="0">
          <stop offset="0" stop-color="var(--silver-dark)"/>
          <stop offset="0.3" stop-color="var(--silver-light)"/>
          <stop offset="0.5" stop-color="var(--silver-mid)"/>
          <stop offset="0.75" stop-color="var(--silver-light)"/>
          <stop offset="1" stop-color="var(--silver-dark)"/>
        </linearGradient>
        <linearGradient id="red-grade" x1="0" y1="0" x2="1" y2="0">
          <stop offset="0" stop-color="var(--red-deep)"/>
          <stop offset="0.4" stop-color="var(--red-bright)"/>
          <stop offset="1" stop-color="var(--red-deep)"/>
        </linearGradient>
        <radialGradient id="red-dot" cx="0.4" cy="0.35" r="0.7">
          <stop offset="0" stop-color="var(--red-bright)"/>
          <stop offset="1" stop-color="var(--red-deep)"/>
        </radialGradient>
      </defs>
      <g clip-path="url(#red-shape)">
        <rect class="sticker-paper" width="680" height="820" fill="url(#red-paper)"/>
        <polygon class="silver-chevron" points="0,235 265,420 500,260 520,305 265,478 0,292" fill="url(#red-silver)"/>
        <polygon class="colour-band" points="0,0 540,0 490,262 265,425 0,238" fill="url(#red-band)"/>
      </g>

      <circle class="brand-dot" cx="70" cy="136" r="26" fill="var(--white)"/>
      <text class="brand-name" x="110" y="160">VESKO</text>
      <text class="range-title" x="243" y="232" text-anchor="middle">LUBRICANTS</text>

      <g class="feature-list">
        <rect x="103" y="246" width="13" height="13" fill="none" stroke="var(--white)" stroke-width="1.6"/>
        <path d="M106,252 l3,4 l8,-10" fill="none" stroke="var(--white)" stroke-width="1.8"/>
        <text class="feature" x="125" y="258">High Performercance Petrol Engine Oil</text>
        <rect x="103" y="268" width="13" height="13" fill="none" stroke="var(--white)" stroke-width="1.6"/>
        <path d="M106,274 l3,4 l8,-10" fill="none" stroke="var(--white)" stroke-width="1.8"/>
        <text class="feature" x="125" y="280">High Full Efficient Petrol Engine Oil</text>
      </g>

      <g class="centre-seal">
        <circle cx="265" cy="418" r="100" fill="var(--white)" stroke="var(--silver-mid)" stroke-width="12"/>
        <text class="seal-name" x="265" y="432" text-anchor="middle" fill="var(--red)">VESKO</text>
      </g>

      <circle class="volume-dot" cx="90" cy="440" r="34" fill="url(#red-dot)" stroke="var(--silver-mid)" stroke-width="4"/>
      <text class="volume" x="90" y="452" text-anchor="middle">5L</text>
      <text class="spec" x="65" y="505">PSI SL / CF</text>
      <text class="spec" x="65" y="527">EMCA A3/B4</text>
      <text class="spec-base" x="65" y="547">MINERAL</text>

      <g class="certificate-badges">
        <circle cx="418" cy="450" r="31" fill="var(--badge-gold)"/>
        <circle cx="485" cy="450" r="28" fill="var(--badge-grey)"/>
        <rect x="388" y="495" width="128" height="48" fill="var(--badge-green)"/>
      </g>

      <text class="grade" x="325" y="695" text-anchor="middle" fill="url(#red-grade)" stroke="var(--white)" stroke-width="3" paint-order="stroke">5W30</text>
      <text class="meets" x="340" y="719" text-anchor="middle">MEETS THE REQUIREMENTS OF:</text>
      <text class="approvals" x="340" y="741" text-anchor="middle">KR 229.7 , TRN M 271 , HLFR 15B110 , ARLEN C4 , NORVIK VDS , TERRAPIN TO-2</text>
    </svg>
  </section>

  <!-- Blue sticker: 20W50 -->
  <section class="sticker sticker--blue" aria-label="Vesko 20W50 sticker">
    <svg viewBox="0 0 680 820" xmlns="http://www.w3.org/2000/svg">
      <defs>
        <clipPath id="blue-shape">
          <path d="M0,45 Q0,0 45,2 L360,40 Q405,50 418,92 L658,710 Q678,772 610,777 L75,800 Q35,802 32,760 L5,120 Z"/>
        </clipPath>
        <linearGradient id="blue-paper" x1="0" y1="0" x2="0" y2="1">
          <stop offset="0.35" stop-color="var(--label-top)"/>
          <stop offset="1" stop-color="var(--label-bottom)"/>
        </linearGradient>
        <linearGradient id="blue-band" x1="0" y1="0" x2="0" y2="1">
          <stop offset="0" stop-color="var(--blue-deep)"/>
          <stop offset="1" stop-color="var(--blue)"/>
        </linearGradient>
        <linearGradient id="blue-silver" x1="0" y1="0" x2="1" y2="0">
          <stop offset="0" stop-color="var(--silver-dark)"/>
          <stop offset="0.3" stop-color="var(--silver-light)"/>
          <stop offset="0.5" stop-color="var(--silver-mid)"/>
          <stop offset="0.75" stop-color="var(--silver-light)"/>
          <stop offset="1" stop-color="var(--silver-dark)"/>
        </linearGradient>
        <linearGradient id="blue-grade" x1="0" y1="0" x2="1" y2="0">
          <stop offset="0" stop-color="var(--blue-deep)"/>
          <stop offset="0.45" stop-color="var(--blue-bright)"/>
          <stop offset="1" stop-color="var(--blue-deep)"/>
        </linearGradient>
        <radialGradient id="blue-dot" cx="0.4" cy="0.35" r="0.7">
          <stop offset="0" stop-color="var(--red-bright)"/>
          <stop offset="1" stop-color="var(--red-deep)"/>
        </radialGradient>
      </defs>
      <g clip-path="url(#blue-shape)">
        <rect class="sticker-paper" width="680" height="820" fill="url(#blue-paper)"/>
        <polygon class="silver-chevron" points="0,235 265,420 500,260 520,305 265,478 0,292" fill="url(#blue-silver)"/>
        <polygon class="colour-band" points="0,0 540,0 490,262 265,425 0,238" fill="url(#blue-band)"/>
      </g>

      <circle class="brand-dot" cx="70" cy="136" r="26" fill="var(--white)"/>
      <text class="brand-name" x="110" y="160">VESKO</text>
      <text class="range-title" x="243" y="232" text-anchor="middle">LUBRICANTS</text>

      <g class="feature-list">
        <rect x="103" y="246" width="13" height="13" fill="none" stroke="var(--white)" stroke-width="1.6"/>
        <path d="M106,252 l3,4 l8,-10" fill="none" stroke="var(--white)" stroke-width="1.8"/>
        <text class="feature" x="125" y="258">High Performercance Petrol Engine Oil</text>
        <rect x="103" y="268" width="13" height="13" fill="none" stroke="var(--white)" stroke-width="1.6"/>
        <path d="M106,274 l3,4 l8,-10" fill="none" stroke="var(--white)" stroke-width="1.8"/>
        <text class="feature" x="125" y="280">High Full Efficient Petrol Engine Oil</text>
      </g>

      <g class="centre-seal">
        <circle cx="265" cy="418" r="100" fill="var(--white)" stroke="var(--silver-mid)" stroke-width="12"/>
        <text class="seal-name" x="265" y="432" text-anchor="middle" fill="var(--blue)">VESKO</text>
      </g>

      <circle class="volume-dot" cx="90" cy="440" r="34" fill="url(#blue-dot)" stroke="var(--silver-mid)" stroke-width="4"/>
      <text class="volume" x="90" y="452" text-anchor="middle">5L</text>
      <text class="spec" x="65" y="505">PSI SL / CF</text>
      <text class="spec" x="65" y="527">EMCA A3/B4</text>
      <text class="spec-base" x="65" y="547">MINERAL</text>

      <g class="certificate-badges">
        <circle cx="418" cy="450" r="31" fill="var(--badge-gold)"/>
        <circle cx="485" cy="450" r="28" fill="var(--badge-grey)"/>
        <rect x="388" y="495" width="128" height="48" fill="var(--badge-green)"/>
      </g>

      <text class="grade" x="325" y="695" text-anchor="middle" fill="url(#blue-grade)" stroke="var(--white)" stroke-width="3" paint-order="stroke">20W50</text>
      <text class="meets" x="340" y="719" text-anchor="middle">MEETS THE REQUIREMENTS OF:</text>
      <text class="approvals" x="340" y="741" text-anchor="middle">KR 229.7 , TRN M 271 , HLFR 15B110 , ARLEN C4 , NORVIK VDS , TERRAPIN TO-2</text>
    </svg>
  </section>

</main>
</body>
</html>
```